Crestline Gas and Plumbing Business Card Design

I am after a business card design for my plumbing business called 'Crestline Gas & Plumbing'. I do all types of plumbing and gas work and specialise in general maintenance plumbing. Would like to see designs using current logo

Industry/Entity Type

Plumbing

Contact Information for Business Card

Name - Dale Whitcombe
Phone number - 0455163027
Email - admin@crestlinegasandplumbing.example.com.au
ABN - 68204915336

```html
<!DOCTYPE html>
<html lang="en">
<head>
<meta charset="utf-8">
<title>Crestline Gas &amp; Plumbing — Business Card</title>
<link href="https://fonts.googleapis.com/css2?family=Open+Sans:wght@400;600;700&display=swap" rel="stylesheet">
<style>
  :root {
    --backdrop: #e9e9e9;
    --card: #ffffff;
    --charcoal: #333333;
    --ink: #2b2b2b;
    --icon-box: #5a5a5a;
    --brand-blue: #1f5fb0;
    --brand-orange: #f28a22;
  }
  * { margin: 0; padding: 0; box-sizing: border-box; }
  html, body {
    width: 1200px; height: 1000px; overflow: hidden;
    background: var(--backdrop);
    font-family: "Open Sans", Arial, sans-serif;
    color: var(--ink);
  }
  .card {
    position: absolute; left: 254px; width: 681px; height: 388px;
    background: var(--card);
  }
  .card--front { top: 93px; }
  .card--back { top: 531px; }

  .brand-panel {
    position: absolute; left: 0; top: 0; width: 297px; height: 100%;
    background: var(--charcoal);
    display: flex; align-items: center; justify-content: center; gap: 10px;
  }
  .brand-panel__mark {
    width: 14px; height: 14px; border-radius: 50%;
    background: var(--brand-orange);
  }
  .brand-panel__name {
    color: #ffffff; font-weight: 700; font-size: 26px; letter-spacing: 1px;
  }

  .contact-name {
    position: absolute; left: 336px; top: 76px;
    font-size: 33px; font-weight: 700; letter-spacing: 1px;
    text-transform: uppercase;
  }
  .abn {
    position: absolute; left: 336px; top: 157px;
    font-size: 18px; font-weight: 600;
  }
  .contact-row { position: absolute; left: 277px; }
  .contact-row--phone { top: 234px; }
  .contact-row--email { top: 292px; }
  .contact-row__icon {
    position: absolute; left: 0; top: 0; width: 42px; height: 41px;
    background: var(--icon-box);
    display: flex; align-items: center; justify-content: center;
  }
  .contact-row__label {
    position: absolute; left: 59px; top: 1px;
    font-size: 15px; font-weight: 700; white-space: nowrap;
  }
  .contact-row__value {
    position: absolute; left: 59px; top: 20px;
    font-size: 15.5px; white-space: nowrap;
  }
  .contact-row--email .contact-row__value { font-size: 14.3px; top: 21px; }

  .brand-lockup {
    position: absolute; left: 0; top: 0; width: 100%; height: 100%;
    display: flex; align-items: center; justify-content: center; gap: 14px;
  }
  .brand-lockup__mark {
    width: 22px; height: 22px; background: var(--brand-blue);
  }
  .brand-lockup__name {
    color: var(--brand-blue); font-weight: 700; font-size: 34px; letter-spacing: 0.5px;
  }
</style>
</head>
<body>
  <section class="card card--front">
    <div class="brand-panel">
      <span class="brand-panel__mark"></span>
      <span class="brand-panel__name">Crestline</span>
    </div>
    <h1 class="contact-name">Dale Whitcombe</h1>
    <p class="abn">ABN - 68204915336</p>

    <div class="contact-row contact-row--phone">
      <div class="contact-row__icon">
        <svg width="18" height="18" viewBox="0 0 24 24" aria-hidden="true">
          <path fill="#ffffff" d="M6.6 10.8c1.4 2.8 3.8 5.1 6.6 6.6l2.2-2.2c.3-.3.7-.4 1-.2 1.1.4 2.3.6 3.6.6.6 0 1 .4 1 1V20c0 .6-.4 1-1 1C10.6 21 3 13.4 3 4c0-.6.4-1 1-1h3.5c.6 0 1 .4 1 1 0 1.3.2 2.5.6 3.6.1.3 0 .7-.2 1z"/>
        </svg>
      </div>
      <span class="contact-row__label">Phone:</span>
      <span class="contact-row__value">0455163027</span>
    </div>

    <div class="contact-row contact-row--email">
      <div class="contact-row__icon">
        <svg width="18" height="14" viewBox="0 0 18 14" aria-hidden="true">
          <rect x="0" y="0" width="18" height="14" rx="1.5" fill="#ffffff"/>
          <path d="M1 1.5 L9 8 L17 1.5" fill="none" stroke="#5a5a5a" stroke-width="1.6"/>
        </svg>
      </div>
      <span class="contact-row__label">Email:</span>
      <span class="contact-row__value">admin@crestlinegasandplumbing.example.com.au</span>
    </div>
  </section>

  <section class="card card--back">
    <div class="brand-lockup">
      <span class="brand-lockup__mark"></span>
      <span class="brand-lockup__name">Crestline Gas &amp; Plumbing</span>
    </div>
  </section>
</body>
</html>
```